Real Estate 24"x24" Sign, Business Card, Letter Head and Envelope

This is a 4 project contest. If we choose a design or designs we like from what you sent we are willing to pay an amount at our discretion for that design even if we don't like all your designs for the 4 projects. Please be creative. Attached are our logo files. Please message us with any questions. Thanks and Good Luck!
Project 1: QLTV Realty 24" x 24" yard sign
We want to use the same blue background in our logo for the sign where the logo in white font will be on. CMYK 100,80,0,0. Attached is a sample a local designer made for you to get an idea what we are looking for. In the sample, the website is way too big and the entire sign is very plain and not attractive looking plus blue color is wrong one. We want the logo on top as large as possible but keeping it proportionate and attractive looking buy not too big that it looks odd. The following information can go in white color background or same blue color background color. Our company colors are blue (as per logo), green (as per logo), and white. "Residential & Commercial" goes under the logo. Under that put our phone number "312-948-6051" as large as possible but still looks good and under that our website in much smaller but readable font "www.qltvrealty.com".
Project 2: Envelope
We have two version of the logo. Use one or both. Whatever looks best in your design. The envelope will be white. We only want on top left corner logo and underneath our mailing address: 5197 Larchmere Ave. Skokie, IL 60093-1725. Maybe some creative decorative design at bottom of envelope will look nice
Project 3: Letter Head
We have two version of the logo. Use one or both. Whatever looks best in your design. We want the following information on the top of the letterhead. Logo, address: 5197 Larchmere Ave., Skokie, IL 60093-1725, phone: 312-948-6051, fax: 312-682-9307 website www.qltvrealty.com, email: info@qltvrealty.com
Project 4: Business card
Use either logo. We need cards for two individuals. Information for Person 1: Dev Kulkarni, Managing Broker, Phone: 312-948-6051, Email: dev.kulkarni@qltvrealty.com. Person 2: Ajay Kulkarni Broker Phone: 312-519-8263 Email: ajay.kulkarni@qltvrealty.com. Add Address, Fax and website same as above letter head.

```html
<!DOCTYPE html>
<html lang="en">
<head>
<meta charset="UTF-8">
<title>QLTV Realty Letterhead</title>
<link href="https://fonts.googleapis.com/css2?family=Arimo:wght@400&family=Montserrat:wght@800&display=swap" rel="stylesheet">
<style>
  :root {
    --brand-blue: #0a3cff;
    --brand-green: #5cf02c;
    --ink: #111111;
    --paper: #ffffff;
  }
  html, body {
    margin: 0;
    padding: 0;
    overflow: hidden;
    background: var(--paper);
  }
  .letterhead {
    position: relative;
    width: 928px;
    height: 1200px;
    overflow: hidden;
    background: var(--paper);
    font-family: "Arimo", Arial, sans-serif;
    color: var(--ink);
  }
  .brand {
    position: absolute;
    left: 78px;
    top: 52px;
    display: flex;
    align-items: center;
    gap: 8px;
  }
  .brand-mark {
    width: 14px;
    height: 14px;
    background: var(--brand-green);
  }
  .brand-name {
    font-family: "Montserrat", Arial, sans-serif;
    font-weight: 800;
    font-size: 24px;
    color: var(--brand-blue);
    line-height: 1;
    width: 120px;
  }
  .address {
    position: absolute;
    left: 224px;
    top: 67px;
    font-family: "Montserrat", Arial, sans-serif;
    font-weight: 800;
    font-size: 17px;
    line-height: 21px;
    color: var(--brand-blue);
  }
  .letter-body {
    position: absolute;
    left: 79px;
    top: 219px;
    width: 752px;
    font-size: 16.4px;
    line-height: 22px;
  }
  .letter-body p {
    margin: 0 0 22px;
  }
  .salutation {
    margin-bottom: 44px !important;
  }
  .closing {
    margin-top: 44px !important;
  }
  .contact-band {
    position: absolute;
    left: 0;
    top: 1102px;
    width: 928px;
    height: 98px;
    background: var(--brand-blue);
    font-family: "Montserrat", Arial, sans-serif;
    font-weight: 800;
    font-size: 14.5px;
    color: var(--paper);
  }
  .contact-item {
    position: absolute;
    top: 40px;
    white-space: nowrap;
  }
  .contact-label {
    color: var(--brand-green);
  }
  .contact-phone { left: 28px; }
  .contact-fax { left: 251px; }
  .contact-web { left: 452px; }
  .contact-email { left: 671px; }
</style>
</head>
<body>
<div class="letterhead">
  <header>
    <div class="brand">
      <span class="brand-mark"></span>
      <span class="brand-name">QLTV Realty</span>
    </div>
    <div class="address">5197 Larchmere Ave.,<br>Skokie, IL 60093-1725</div>
  </header>

  <main class="letter-body">
    <p class="salutation">To whom it may concern,</p>
    <p>Lorem ipsum dolor sit amet, consectetur adipiscing elit. Praesent nunc ipsum, vehicula sed neque non, dictum luctus eros. Sed ut maximus ligula. Nullam sit amet iaculis nibh. In imperdiet erat a eros bibendum dignissim. In viverra ullamcorper augue, eu suscipit odio molestie eu. Vivamus sit amet ligula ut elit dignissim lacinia a ut turpis. Duis bibendum, nulla quis ultrices tincidunt, augue odio luctus lectus, sit amet tempor nunc nunc quis justo. Nullam vehicula metus vitae consequat placerat. Suspendisse sit amet enim leo. In eu metus sit amet metus sollicitudin aliquam porttitor eget lectus.</p>
    <p>Suspendisse bibendum est sit amet luctus dignissim. Morbi posuere ipsum a finibus aliquam. Donec mattis accumsan mi, eget egestas leo interdum et. Suspendisse molestie tortor consectetur magna venenatis congue vel a felis. Vestibulum ante ipsum primis in faucibus orci luctus et ultrices posuere cubilia Curae; Nam non felis venenatis nisi viverra bibendum. Proin pharetra vulputate tellus egestas condimentum. Phasellus bibendum, elit id molestie ornare, massa justo tempus magna, ac dapibus eros massa eu ipsum. Mauris fringilla nunc sem, in sollicitudin orci viverra sed. Fusce pretium erat vitae lorem malesuada, quis tempus dolor condimentum. Sed suscipit ipsum metus, in consectetur velit faucibus id.</p>
    <p>Cras posuere orci eu risus pretium molestie. Maecenas at orci ac dui ultrices malesuada. Fusce dignissim, tortor vel interdum accumsan, mi nibh efficitur sapien, ut tempor elit massa et nulla. Proin quis sollicitudin dolor. Pellentesque finibus a enim hendrerit tristique. Cras fringilla scelerisque urna, quis ullamcorper mi molestie quis. Pellentesque sed est nisi. Fusce venenatis mi neque, tempus molestie metus volutpat id. Cras eget dolor lacinia, ultricies sem in, rhoncus ex. Etiam efficitur ac tortor vel lacinia. Pellentesque sapien metus, accumsan id tincidunt vitae, sollicitudin nec tortor. Mauris vitae nisi eu odio maximus ornare. Integer pulvinar ligula ullamcorper commodo consectetur.</p>
    <p class="closing">Yours Sincerely,</p>
    <p>Dev Kulkarni and Ajay Kulkarni<br>QLTV Realty</p>
  </main>

  <footer class="contact-band">
    <span class="contact-item contact-phone"><span class="contact-label">Phone:</span> 312-948-6051</span>
    <span class="contact-item contact-fax"><span class="contact-label">Fax:</span> 312-682-9307</span>
    <span class="contact-item contact-web"><span class="contact-label">Web:</span> qltvrealty.com</span>
    <span class="contact-item contact-email"><span class="contact-label">Email:</span> info@qltvrealty.com</span>
  </footer>
</div>
</body>
</html>
```